BRINDLEMARK STUDIOS PRODUCT CATALOG

Rustic and Elegant Boutique Custom and personalized furniture and Kitchen accessories with a contemporary art Flair. My product is very personable. I put an effort into everyone like it is my own. From Western red cedar toWestern red cedar to Eastern giant Bonzai. Are use word from all over the world. Including,Eastern Mauyi Bonzai. I use wood from all over the world. And can do custom orders for Desired . I make style tables that include varnish is on some of the more beautiful pieces of wood natural and some of the others I turn into river tables or waterfall tables. This involves a lot of coloured Apoxsee and many hours ofI make style tables that include varnish is on some of the more beautiful pieces of wood natural and some of the others I turn into river tables or waterfall tables. This involves a lot of epoxy and many hours of work mixing colours or sanding down the curve to the perfect circumference at the end of the day each one is a piece of art in itself generally 56 feet and legsmixing colours or sanding down the curve to the perfect circumference at the end of the day each one is a piece of art in itself. In my practice I also use a lot of original woodworking tools from the 30s and 40s. Not allIn my practice I also use a lot of original woodworking tools from the 30s to 70s. I also produce in tables hallway tables sofa tables boardroom tables and all actuality I can make any table you want it'll just be one of a kind. A cut above, like none other.

Target Market(s)

The elite. Higher and then a class above. Affluent Female home owners. High end interior designers. Exclusive corporate gifts and furnishings .

Industry/Entity Type

Home Furnishing

Font styles to use
Other font styles liked:
• See attached branding board.

Requirements
Must have
• My logo Black & Gold big on cover subtly next to page #'s on outside corners on every page. Matte Cover page then glossy inside catalog. Source file included. One product per page for larger pieces. Along with multiple small pieces per page. Leave room for write up for each pice.
Must convey sophisticated yet down to earth. Emphasis on each pieces uniqueness and story. Use colours from attached branding board.
Nice to have
• Having the smaller pieces on pages formatted vertically along side of pages.
Should not have
• Avoid looking too over bearing or flashy.

```html
<!DOCTYPE html>
<html lang="en">
<head>
<meta charset="utf-8">
<title>Brindlemark Studios Catalog 2020-2021</title>
<link rel="stylesheet" href="https://fonts.googleapis.com/css2?family=Montserrat:wght@400;500;600;700&display=swap">
<style>
  :root{
    --stage:#5e5e67;
    --paper:#f4f4f4;
    --paper-edge:#e2e2e2;
    --ink:#4a4a4a;
    --ink-soft:#8a8a8a;
    --rule:#bdbdbd;
    --photo-grey:#d9d9d9;
    --wood-light:#e8a92e;
    --wood-deep:#b9681f;
    --grass:#5c7a2c;
    --aqua:#dcebea;
  }
  *{margin:0;padding:0;box-sizing:border-box}
  html,body{width:1200px;height:4461px;overflow:hidden;background:var(--stage)}
  body{font-family:"Montserrat",sans-serif;color:var(--ink)}
  .sheet{position:relative;width:1200px;height:892px}
  .sheet:last-child{height:893px}
  .page{position:absolute;background:var(--paper);box-shadow:0 18px 40px rgba(0,0,0,.35)}
  .spread{position:absolute;left:160px;top:196px;width:880px;height:500px;display:flex;box-shadow:0 18px 40px rgba(0,0,0,.35)}
  .spread .half{position:relative;width:440px;height:500px;background:var(--paper);overflow:hidden}
  .spread .half.left{border-right:1px solid var(--paper-edge)}
  .photo{position:absolute}
  .photo.wood{background:linear-gradient(135deg,#f3c55a,var(--wood-light) 45%,var(--wood-deep))}
  .photo.studio{background:linear-gradient(160deg,#f0f0f0,var(--photo-grey))}

  /* cover */
  .cover{left:340px;top:136px;width:520px;height:620px}
  .cover .title{position:absolute;left:130px;top:52px;width:340px;text-align:right;font-weight:700;font-size:30px;letter-spacing:3px;line-height:1.05;color:#555}
  .cover .shot{left:100px;top:150px;width:340px;height:360px;background:linear-gradient(160deg,#f2f2f2,#cfcfcf)}
  .cover .shot .piece{position:absolute;left:60px;top:110px;width:220px;height:120px;background:linear-gradient(120deg,#f6cd5b,var(--wood-light) 55%,#c9822a)}
  .vert{position:absolute;writing-mode:vertical-rl;font-size:15px;letter-spacing:6px}
  .cover .catalog{right:28px;top:170px;font-weight:500}
  .cover .year{left:40px;top:170px;letter-spacing:2px;transform:rotate(180deg)}
  .cover .web{position:absolute;right:80px;bottom:40px;font-size:11px;letter-spacing:1px;color:var(--ink-soft)}

  /* contents */
  .contents h2{position:absolute;left:60px;top:60px;font-size:24px;font-weight:700;color:#555}
  .contents h2::after{content:"";display:block;width:60px;height:2px;background:var(--ink);margin-top:6px}
  .toc{position:absolute;left:60px;top:130px;width:320px;list-style:none}
  .toc li{display:flex;justify-content:space-between;font-size:12px;color:var(--ink-soft);padding:6px 0;border-bottom:1px solid var(--rule)}

  /* introduction */
  .intro h2{position:absolute;left:50px;top:130px;font-size:22px;font-weight:700;color:#555}
  .intro h2::after{content:"";display:block;width:60px;height:2px;background:var(--ink);margin-top:6px}
  .intro p{position:absolute;left:50px;top:185px;width:330px;font-size:11px;line-height:1.6;color:var(--ink-soft)}

  /* product */
  .product .left{background:var(--aqua)}
  .price{position:absolute;left:200px;top:70px;font-size:18px;color:#555}
  .price-line{position:absolute;left:165px;top:80px;width:30px;height:70px;border-left:1px solid #999;border-top:1px solid #999}
  .product h2{position:absolute;left:50px;top:50px;font-size:20px;font-weight:700;color:#555}
  .product p.body{position:absolute;left:50px;top:95px;width:340px;font-size:11px;line-height:1.6;color:var(--ink-soft)}
  .thumb{position:absolute;top:270px;width:150px;height:100px}
  .caption{position:absolute;top:385px;width:150px;font-size:10px;line-height:1.5;color:var(--ink-soft)}

  /* back cover */
  .back{left:340px;top:136px;width:520px;height:620px}
  .back .title{position:absolute;left:50px;top:420px;font-weight:700;font-size:26px;letter-spacing:3px;line-height:1.05;color:#555}
  .contact{position:absolute;left:50px;top:510px;display:grid;grid-template-columns:auto auto;gap:10px 40px;font-size:11px;color:var(--ink-soft)}
  .contact span{display:flex;align-items:center;gap:8px}
  .contact .phone{font-size:16px;color:var(--ink);font-weight:600}
  svg{flex:none}
</style>
</head>
<body>

<section class="sheet">
  <div class="page cover">
    <div class="title">BRINDLEMARK<br>STUDIOS</div>
    <div class="vert year">2020-2021</div>
    <div class="photo shot" role="img" aria-label="Photograph of a golden cedar table with hairpin legs">
      <div class="piece"></div>
    </div>
    <div class="vert catalog">• CATALOG •</div>
    <div class="web">www.brindlemarkstudios.com</div>
  </div>
</section>

<section class="sheet">
  <div class="spread contents">
    <div class="half left">
      <div class="photo studio" style="inset:30px 0 30px 30px" role="img" aria-label="Photograph of two polished cedar slab tables in a studio"></div>
      <div class="photo wood" style="left:120px;top:70px;width:140px;height:330px" role="img" aria-label="Cedar slab table top"></div>
    </div>
    <div class="half right">
      <h2>Content</h2>
      <ol class="toc">
        <li>Lorem ipsum dolor<span>1</span></li>
        <li>Lorem ipsum dolor<span>2</span></li>
        <li>Lorem ipsum dolor<span>3</span></li>
        <li>Lorem ipsum dolor<span>4</span></li>
        <li>Lorem ipsum dolor<span>5</span></li>
        <li>Lorem ipsum dolor<span>6</span></li>
        <li>Lorem ipsum dolor<span>7</span></li>
        <li>Lorem ipsum dolor<span>8</span></li>
        <li>Lorem ipsum dolor<span>9</span></li>
        <li>Lorem ipsum dolor<span>10</span></li>
        <li>Lorem ipsum dolor<span>11</span></li>
      </ol>
    </div>
  </div>
</section>

<section class="sheet">
  <div class="spread intro">
    <div class="half left">
      <h2>Introduction</h2>
      <p>Every piece begins with a slab chosen by hand for its grain, knots and character. We work cedar, bonsai burl and rare timbers from around the world, finishing some in clear varnish and pouring others into river and waterfall tables. Each table is sanded, shaped and oiled in our workshop with tools dating back to the thirties, so no two are ever alike.</p>
    </div>
    <div class="half right">
      <div class="photo wood" style="left:0;top:0;width:440px;height:240px;background:linear-gradient(150deg,#efe9dd 0 30%,#c46a22 30% 70%,#e9b04a)" role="img" aria-label="Photograph of a varnished live edge table"></div>
      <div class="photo" style="left:0;top:250px;width:215px;height:250px;background:linear-gradient(160deg,#6f8f35,var(--grass))" role="img" aria-label="Photograph of a slab bench on grass"></div>
      <div class="photo" style="left:225px;top:250px;width:215px;height:250px;background:linear-gradient(90deg,var(--grass),#d99a4a 25% 75%,var(--grass))" role="img" aria-label="Photograph of a cedar slab with knots"></div>
    </div>
  </div>
</section>

<section class="sheet">
  <div class="spread product">
    <div class="half left">
      <div class="price-line"></div>
      <div class="price">$350</div>
      <div class="photo" style="left:30px;top:190px;width:400px;height:90px;background:linear-gradient(180deg,#e0a13a,#7dbb63 45%,#e0a13a)" role="img" aria-label="Photograph of a cedar bench with a green epoxy river"></div>
    </div>
    <div class="half right">
      <h2>Product Details</h2>
      <p class="body">A live edge cedar bench with a green epoxy river running through its heart. The slab was air dried for two years, then cut, poured and polished by hand. Clear satin finish, steel hairpin legs. Length 180 cm, depth 40 cm.</p>
      <div class="photo wood thumb" style="left:50px" role="img" aria-label="Close-up of varnished cedar grain"></div>
      <div class="photo wood thumb" style="left:230px;background:linear-gradient(135deg,#c9752a,#e6b25a,#9d5419)" role="img" aria-label="Close-up of resin filled knots"></div>
      <div class="caption" style="left:50px">Natural knots sealed under a satin varnish.</div>
      <div class="caption" style="left:230px">Resin filled cracks polished to a soft glow.</div>
    </div>
  </div>
</section>

<section class="sheet">
  <div class="page back">
    <div class="title">BRINDLEMARK<br>STUDIOS</div>
    <div class="contact">
      <span class="phone"><svg width="14" height="14" viewBox="0 0 24 24"><path d="M6.6 10.8a15 15 0 0 0 6.6 6.6l2.2-2.2a1 1 0 0 1 1-.3 11 11 0 0 0 3.6.6 1 1 0 0 1 1 1V20a1 1 0 0 1-1 1A17 17 0 0 1 3 4a1 1 0 0 1 1-1h3.5a1 1 0 0 1 1 1c0 1.2.2 2.4.6 3.6a1 1 0 0 1-.3 1z" fill="#4a4a4a"/></svg>604 555 0187</span>
      <span><svg width="12" height="12" viewBox="0 0 24 24"><path d="M12 2a7 7 0 0 0-7 7c0 5 7 13 7 13s7-8 7-13a7 7 0 0 0-7-7zm0 9.5A2.5 2.5 0 1 1 12 6.5a2.5 2.5 0 0 1 0 5z" fill="#8a8a8a"/></svg>Your address here</span>
      <span><svg width="12" height="12" viewBox="0 0 24 24"><rect x="2" y="5" width="20" height="14" rx="2" fill="none" stroke="#8a8a8a" stroke-width="2"/><path d="M2 6l10 7 10-7" fill="none" stroke="#8a8a8a" stroke-width="2"/></svg>hello@brindlemarkstudios.com</span>
      <span><svg width="12" height="12" viewBox="0 0 24 24"><circle cx="12" cy="12" r="9" fill="none" stroke="#8a8a8a" stroke-width="2"/><path d="M3 12h18M12 3c3 3 3 15 0 18M12 3c-3 3-3 15 0 18" fill="none" stroke="#8a8a8a" stroke-width="1.5"/></svg>www.brindlemarkstudios.com</span>
    </div>
  </div>
</section>

</body>
</html>
```